Owner of Clinical Testing Lab/. Pixel Harbor Logo completed. Need Matching business Cards

Im the owner of and need cards for business. Colors fonts and logo already purchased through pixel harbur and have the source files. Like to keep same color format , Include logo one side. My Name Address of Lab. My cell number, Lab telephone number and website address. Want to keep simple.

Target Market(s)

Customers

Industry/Entity Type

HealthCare

Contact Information for Business Card

Dr. Corabel Fensworth Ph.D. Address: KTR Meridian Yard 4120 Larkfield Commons Way Building 2600 Room 245. Baton Rouge LA 70993. Phone : 318.555.0193

Requirements
Must have
• Logo - Color same

```html
<!DOCTYPE html>
<html lang="en">
<head>
<meta charset="utf-8">
<title>Lumenar Laboratories – Business Cards</title>
<link rel="stylesheet" href="https://fonts.googleapis.com/css2?family=Montserrat:wght@700&family=Questrial&display=swap">
<style>
  :root {
    --backdrop: #d6d6d6;
    --card-blue: #0d5592;
    --card-blue-deep: #0a467b;
    --card-white: #ffffff;
    --accent-teal: #5cc6aa;
    --brand-navy: #1b4f8e;
    --text-light: #ffffff;
    --rule-light: rgba(255, 255, 255, 0.28);
  }
  * { box-sizing: border-box; margin: 0; padding: 0; }
  html, body {
    width: 1200px;
    height: 800px;
    overflow: hidden;
    background: var(--backdrop);
    font-family: "Questrial", "Century Gothic", sans-serif;
  }
  .canvas {
    width: 1200px;
    height: 800px;
    display: flex;
    align-items: center;
    justify-content: center;
    gap: 120px;
  }
  .card {
    width: 340px;
    height: 580px;
    border-radius: 2px;
    box-shadow: 0 14px 30px rgba(0, 0, 0, 0.18);
    position: relative;
  }

  /* Front: contact side */
  .card-front {
    background: radial-gradient(circle at 40% 30%, var(--card-blue) 0%, var(--card-blue-deep) 100%);
    color: var(--text-light);
    padding: 0 34px;
  }
  .front-brand {
    height: 250px;
    display: flex;
    flex-direction: column;
    align-items: center;
    justify-content: center;
    gap: 14px;
  }
  .brand-dot {
    width: 20px;
    height: 20px;
    border-radius: 50%;
    background: var(--accent-teal);
  }
  .front-brand .brand-name {
    font-size: 27px;
    letter-spacing: 3px;
    text-align: center;
    line-height: 1.25;
    color: var(--text-light);
  }
  .rule {
    border: none;
    border-top: 1px solid var(--rule-light);
    margin: 0;
  }
  .holder {
    padding: 20px 0 18px;
  }
  .holder-name {
    font-family: "Montserrat", "Century Gothic", sans-serif;
    font-weight: 700;
    font-size: 19px;
    margin-bottom: 12px;
  }
  .holder-address {
    font-style: normal;
    font-size: 16px;
    line-height: 1.42;
  }
  .contact-list {
    list-style: none;
    padding-top: 18px;
    display: flex;
    flex-direction: column;
    gap: 7px;
  }
  .contact-item {
    display: flex;
    align-items: center;
    gap: 10px;
    font-size: 15px;
  }
  .contact-icon {
    width: 20px;
    height: 20px;
    flex: none;
  }

  /* Back: brand side */
  .card-back {
    background: var(--card-white);
    display: flex;
    flex-direction: column;
    align-items: center;
    justify-content: center;
  }
  .back-brand {
    display: flex;
    align-items: center;
    gap: 12px;
    margin-top: -40px;
  }
  .back-brand .brand-name {
    font-size: 24px;
    letter-spacing: 2px;
    line-height: 1.25;
    color: var(--brand-navy);
  }
  .back-website {
    position: absolute;
    right: 26px;
    bottom: 28px;
    font-size: 14px;
    color: var(--brand-navy);
  }
</style>
</head>
<body>
<main class="canvas">

  <section class="card card-front" aria-label="Business card front">
    <div class="front-brand">
      <span class="brand-dot"></span>
      <p class="brand-name">LUMENAR<br>LABORATORIES</p>
    </div>
    <hr class="rule">
    <div class="holder">
      <h1 class="holder-name">Dr. Corabel Fensworth Ph.D.</h1>
      <address class="holder-address">
        KTR Meridian Yard 4120<br>
        Larkfield Commons Way<br>
        Building 2600 Room 245<br>
        Baton Rouge LA 70993
      </address>
    </div>
    <hr class="rule">
    <ul class="contact-list">
      <li class="contact-item">
        <svg class="contact-icon" viewBox="0 0 20 20" aria-hidden="true">
          <circle cx="10" cy="10" r="10" fill="var(--accent-teal)"/>
          <path d="M6.5 5.5l2 0 1 2.5-1.3 1a6 6 0 0 0 2.8 2.8l1-1.3 2.5 1v2a1 1 0 0 1-1 1A8 8 0 0 1 5.5 6.5a1 1 0 0 1 1-1z" fill="#fff"/>
        </svg>
        <span>Lab : 318.555.0193</span>
      </li>
      <li class="contact-item">
        <svg class="contact-icon" viewBox="0 0 20 20" aria-hidden="true">
          <circle cx="10" cy="10" r="10" fill="var(--accent-teal)"/>
          <rect x="7" y="4.5" width="6" height="11" rx="1" fill="none" stroke="#fff" stroke-width="1.4"/>
          <circle cx="10" cy="13.4" r="0.7" fill="#fff"/>
        </svg>
        <span>318.555.0193</span>
      </li>
      <li class="contact-item">
        <svg class="contact-icon" viewBox="0 0 20 20" aria-hidden="true">
          <circle cx="10" cy="10" r="10" fill="var(--accent-teal)"/>
          <rect x="5" y="6.5" width="10" height="7" fill="none" stroke="#fff" stroke-width="1.3"/>
          <path d="M5 6.5l5 4 5-4" fill="none" stroke="#fff" stroke-width="1.3"/>
        </svg>
        <span>info@lumenarlaboratories.com</span>
      </li>
      <li class="contact-item">
        <svg class="contact-icon" viewBox="0 0 20 20" aria-hidden="true">
          <circle cx="10" cy="10" r="10" fill="var(--accent-teal)"/>
          <circle cx="10" cy="10" r="5" fill="none" stroke="#fff" stroke-width="1.2"/>
          <ellipse cx="10" cy="10" rx="2.2" ry="5" fill="none" stroke="#fff" stroke-width="1"/>
          <path d="M5 10h10" stroke="#fff" stroke-width="1"/>
        </svg>
        <span>www.lumenarlaboratories.com</span>
      </li>
    </ul>
  </section>

  <section class="card card-back" aria-label="Business card back">
    <div class="back-brand">
      <span class="brand-dot"></span>
      <p class="brand-name">LUMENAR<br>LABORATORIES</p>
    </div>
    <p class="back-website">www.lumenarlaboratories.com</p>
  </section>

</main>
</body>
</html>
```